Tulip Orchard Wares webdesign + corecommerce implementation

Hi there!
We are a brand new small company located in central Europe, specializing in handmade coffee and tea mugs - please check www.tuliporchardwares.com

We are looking for a complete redesign, something easy, nothing complicated.

1. web desing (smooth and easy - homepage,product detail page, etc...)
2. html/css
3. corecommerce platform implementation

```html
<!DOCTYPE html>
<html lang="en">
<head>
<meta charset="utf-8">
<title>Tulip Orchard Wares – Handmade Mugs</title>
<link href="https://fonts.googleapis.com/css2?family=Arimo:wght@400;700&family=Mulish:wght@400;600;700&family=Playfair+Display:ital,wght@1,700&display=swap" rel="stylesheet">
<style>
:root{
  --page:#f6eee2;
  --paper:#fdfaf5;
  --brown:#8a5a24;
  --brown-dark:#6b4417;
  --ink:#3a2a1a;
  --link:#6b3a12;
  --grey-text:#9a9a9a;
  --panel:#4a4a4a;
  --panel-dark:#3a3a3a;
  --panel-light:#efebe6;
  --price:#7b4f1f;
  --white:#ffffff;
}
*{box-sizing:border-box;margin:0;padding:0}
html,body{width:1022px;height:1200px;overflow:hidden}
body{background:radial-gradient(circle at 0 0,#efe3d0 0,var(--page) 300px);font-family:Arimo,Arial,sans-serif;color:var(--ink);position:relative}
a{color:inherit;text-decoration:none}
.abs{position:absolute}

/* top utility */
.account-bar{left:675px;top:0;width:271px;height:33px;background:linear-gradient(#555,#333);border-radius:0 0 3px 3px;display:flex;align-items:center;justify-content:center;gap:8px;color:#ddd;font-size:11px}
.account-bar .sep{color:#999}
.account-bar svg{width:12px;height:12px;vertical-align:-2px;margin-right:3px}
.search{left:571px;top:49px;width:143px;height:24px;background:var(--white);border:1px solid #ccc;font-size:10px;padding:6px 11px;color:#333}
.search svg{position:absolute;right:8px;top:5px;width:13px;height:13px}
.cart{left:725px;top:44px;width:206px;height:31px;background:var(--white);border-radius:3px;box-shadow:0 1px 3px rgba(0,0,0,.15);font-size:14px;display:flex;align-items:center;padding-left:12px;gap:10px;color:#444}
.cart strong{color:#b3261e}

/* header */
.header{left:76px;top:86px;width:870px;height:66px;background:linear-gradient(#a06a2c,#7c4f1d);border-radius:3px 3px 0 0}
.logo-cup{left:182px;top:16px;width:96px;height:96px;border-radius:50%;background:var(--white)}
.logo{left:91px;top:86px;width:278px;height:65px;background:var(--white);border-radius:32px 32px 0 0;display:flex;flex-direction:column;align-items:center;justify-content:center}
.logo .name{font-family:Mulish,sans-serif;font-weight:600;font-size:24px;color:#5a3a1c;line-height:1}
.logo .tag{font-family:Mulish,sans-serif;font-weight:600;font-size:12px;color:#5a3a1c;margin-top:4px}
.nav{left:430px;top:110px;display:flex;font-size:13px;color:var(--white)}
.nav a{padding:0 10px;border-left:1px solid rgba(255,255,255,.3)}
.nav a:first-child{border:0;text-decoration:underline}

/* main */
.main{left:76px;top:151px;width:870px;height:958px;background:var(--paper)}
.slider{left:85px;top:158px;width:852px;height:295px;background:#ece7e1;box-shadow:0 8px 12px -8px rgba(0,0,0,.25)}
.slide-photo{left:91px;top:162px;width:841px;height:285px;background:linear-gradient(180deg,#6f6f6f 0,#8a8a8a 35%,#a8584a 50%,#b06a55 70%,#8f7a66 100%)}
.slide-title{left:91px;top:187px;width:841px;text-align:center;color:var(--white);font-size:24px}
.slide-title em{font-family:"Playfair Display",serif;font-weight:700;font-size:28px;margin-left:6px}
.slide-arrow{top:286px;width:35px;height:35px;border-radius:50%;background:var(--white);display:flex;align-items:center;justify-content:center}
.slide-arrow svg{width:12px;height:14px}
.intro{left:100px;top:485px;width:822px;text-align:center;font-family:Mulish,sans-serif;font-weight:600;font-size:17px;line-height:25px;color:var(--grey-text)}
.divider{left:89px;top:559px;width:844px;border-top:1px dashed #bbb}

/* featured */
.featured{left:89px;top:577px;width:568px;height:523px;background:var(--panel-light);border-radius:4px;overflow:hidden}
.panel-head{height:46px;background:linear-gradient(#555,#3a3a3a);color:#eee;font-family:Mulish,sans-serif;font-weight:700;font-size:15px;display:flex;align-items:center;padding:0 18px}
.sort{margin-left:auto;font-family:Arimo,sans-serif;font-weight:400;font-size:10px;color:var(--white);display:flex;align-items:center;gap:6px}
.sort .select{width:117px;height:24px;background:var(--white);color:#666;padding:6px 10px;position:relative}
.sort .select:after{content:"";position:absolute;right:8px;top:9px;border:5px solid transparent;border-top:6px solid #666}
.card{width:166px;height:196px;background:var(--white);padding:5px}
.card .photo{height:102px;position:relative}
.card .price{position:absolute;right:0;bottom:-1px;width:38px;height:38px;border-radius:50%;background:var(--price);border:2px solid var(--white);color:var(--white);font-size:12px;display:flex;align-items:center;justify-content:center}
.card .title{font-size:11.5px;color:var(--link);line-height:16px;margin:9px 0 0 3px;height:40px}
.card .title span{white-space:nowrap}
.card .buy{margin:5px 0 0 4px;width:148px;height:30px;background:linear-gradient(#9a6630,#7a4c1c);color:var(--white);font-size:12px;font-weight:700;display:flex;align-items:center;justify-content:center;gap:8px}
.card .buy svg{width:18px;height:15px}
.pager{left:347px;top:1064px;display:flex;gap:3px;align-items:center;font-size:9px;color:#555}
.pager span.p{width:20px;height:19px;border-radius:3px;background:#d9d4ce;color:#999;display:flex;align-items:center;justify-content:center}
.pager span.on{background:#888;color:var(--white)}

/* country */
.country{left:667px;top:577px;width:265px;height:327px;background:var(--panel);border:3px solid var(--panel-dark);border-radius:4px}
.country h3{font-family:Mulish,sans-serif;font-weight:700;font-size:16px;color:#eee;padding:13px 14px 10px;border-bottom:1px solid #5e5e5e;margin:0 5px}
.list{display:grid;grid-template-columns:118px 1fr;list-style:none;padding:6px 0 0 12px;row-gap:9px;font-size:11px;color:var(--white);white-space:nowrap}
.country .list{padding-top:12px;row-gap:14px}
.list li:before{content:"";display:inline-block;border:3px solid transparent;border-left:4px solid #aaa;margin-right:7px}
.map{position:absolute;left:7px;top:170px;width:245px;height:145px;border-top:1px solid #5e5e5e;background:linear-gradient(160deg,#55524d,#6a645b)}
.categories{left:677px;top:928px;width:246px}
.categories h3{font-family:Mulish,sans-serif;font-weight:700;font-size:17px;color:var(--brown);padding:0 7px 11px;border-bottom:1px solid #ccc}
.categories .list{grid-template-columns:116px 1fr;color:var(--ink);font-size:13.5px;row-gap:11px;padding:11px 0 0 10px}

/* footer */
.footer-nav{left:76px;top:1133px;font-size:11px;color:#222;display:flex;gap:8px}
.copyright{left:76px;top:1162px;font-size:11px;color:#222}
.social{top:1133px;width:38px;height:38px;border-radius:50%;background:radial-gradient(circle at 40% 35%,#f0c36a,#c98a1e)}
</style>
</head>
<body>

<div class="abs account-bar">
  <a href="#"><svg viewBox="0 0 12 12"><circle cx="6" cy="3.5" r="3" fill="#ddd"/><path d="M0 12c0-4 12-4 12 0z" fill="#ddd"/></svg>My Account</a><span class="sep">|</span>
  <a href="#"><svg viewBox="0 0 12 12"><rect x="1" y="1" width="10" height="10" fill="none" stroke="#ddd"/><path d="M3 6l2 2 5-6" fill="none" stroke="#ddd" stroke-width="1.5"/></svg>Check Out</a><span class="sep">|</span>
  <a href="#"><svg viewBox="0 0 12 12"><path d="M3 6V4a3 3 0 016 0v2" fill="none" stroke="#ddd" stroke-width="1.5"/><rect x="2" y="6" width="8" height="6" fill="#ddd"/></svg>Logout</a>
</div>
<div class="abs search">Search<svg viewBox="0 0 13 13"><circle cx="5" cy="5" r="4" fill="none" stroke="#222" stroke-width="2"/><path d="M8 8l4 4" stroke="#222" stroke-width="2.5"/></svg></div>
<div class="abs cart"><svg width="22" height="18" viewBox="0 0 22 18"><path d="M1 1h4l3 11h11l2-8H6" fill="none" stroke="#d23a3a" stroke-width="1.5"/><circle cx="9" cy="15.5" r="1.5" fill="#d23a3a"/><circle cx="17" cy="15.5" r="1.5" fill="#d23a3a"/></svg><span><strong>0</strong> item(s) &nbsp;/&nbsp; Total : <strong>$0.00</strong></span></div>

<div class="abs header"></div>
<div class="abs logo-cup"></div>
<div class="abs logo"><span class="name">Tulip Orchard Wares</span><span class="tag">Instant connection</span></div>
<nav class="abs nav"><a href="#">Home</a><a href="#">Categories</a><a href="#">New Arrivals</a><a href="#">About our mugs</a><a href="#">My Account</a><a href="#">Contact Us</a></nav>

<div class="abs main"></div>
<div class="abs slider"></div>
<div class="abs slide-photo" role="img" aria-label="Three handmade terracotta mugs painted with daisies and tulips on a woven mat"></div>
<div class="abs slide-title">Relax and <em>"Mug the moment"!</em></div>
<div class="abs slide-arrow" style="left:103px"><svg viewBox="0 0 12 14"><path d="M9 1L3 7l6 6" fill="none" stroke="#999" stroke-width="1.5"/></svg></div>
<div class="abs slide-arrow" style="left:884px"><svg viewBox="0 0 12 14"><path d="M3 1l6 6-6 6" fill="none" stroke="#999" stroke-width="1.5"/></svg></div>

<p class="abs intro">Hey coffee lovers! Looking for a unique coffee mug? We offer beautiful handmade coffee mugs and tea cups born in the heart of Europe. Beautiful design, precise execution and piece of a heart.</p>
<div class="abs divider"></div>

<section class="abs featured">
  <div class="panel-head">Featured Products<div class="sort">Sort by : <div class="select">Most Recent</div></div></div>
</section>

<div class="abs card" style="left:102px;top:635px"><div class="photo" role="img" aria-label="Terracotta mug with white daisies" style="background:linear-gradient(#c47a66,#a05a48 60%,#9c8670)"><span class="price">$28</span></div><p class="title"><span>Cappuccino mug with daisies</span><br>(empty decor)</p><a class="buy" href="#"><svg viewBox="0 0 18 15"><path d="M1 1h3l2 8h9l2-6H5" fill="none" stroke="#fff" stroke-width="1.5"/><circle cx="7" cy="13" r="1.4" fill="#fff"/><circle cx="14" cy="13" r="1.4" fill="#fff"/></svg>ADD TO CART</a></div>
<div class="abs card" style="left:292px;top:635px"><div class="photo" role="img" aria-label="Cream mug with painted cat" style="background:linear-gradient(#7c7c7c,#d8d3b4 55%,#9c8670)"><span class="price">$28</span></div><p class="title"><span>Cappuccino mug with daisies</span><br>(empty decor)</p><a class="buy" href="#"><svg viewBox="0 0 18 15"><path d="M1 1h3l2 8h9l2-6H5" fill="none" stroke="#fff" stroke-width="1.5"/><circle cx="7" cy="13" r="1.4" fill="#fff"/><circle cx="14" cy="13" r="1.4" fill="#fff"/></svg>ADD TO CART</a></div>
<div class="abs card" style="left:480px;top:635px"><div class="photo" role="img" aria-label="Red mug with coffee bean pattern" style="background:linear-gradient(90deg,#f3f3f3,#c86a4a 50%,#a8201a)"><span class="price">$28</span></div><p class="title"><span>Cappuccino mug with daisies</span><br>(empty decor)</p><a class="buy" href="#"><svg viewBox="0 0 18 15"><path d="M1 1h3l2 8h9l2-6H5" fill="none" stroke="#fff" stroke-width="1.5"/><circle cx="7" cy="13" r="1.4" fill="#fff"/><circle cx="14" cy="13" r="1.4" fill="#fff"/></svg>ADD TO CART</a></div>
<div class="abs card" style="left:102px;top:849px"><div class="photo" role="img" aria-label="White mug with heart motif" style="background:linear-gradient(#7a7a7a,#c8c4c0 50%,#9c8670)"><span class="price">$28</span></div><p class="title"><span>Cappuccino mug with daisies</span><br>(empty decor)</p><a class="buy" href="#"><svg viewBox="0 0 18 15"><path d="M1 1h3l2 8h9l2-6H5" fill="none" stroke="#fff" stroke-width="1.5"/><circle cx="7" cy="13" r="1.4" fill="#fff"/><circle cx="14" cy="13" r="1.4" fill="#fff"/></svg>ADD TO CART</a></div>
<div class="abs card" style="left:292px;top:849px"><div class="photo" role="img" aria-label="Mug with red and black zigzag stripes" style="background:linear-gradient(#7a7a7a,#b8483a 45%,#9c8670)"><span class="price">$28</span></div><p class="title"><span>Cappuccino mug with daisies</span><br>(empty decor)</p><a class="buy" href="#"><svg viewBox="0 0 18 15"><path d="M1 1h3l2 8h9l2-6H5" fill="none" stroke="#fff" stroke-width="1.5"/><circle cx="7" cy="13" r="1.4" fill="#fff"/><circle cx="14" cy="13" r="1.4" fill="#fff"/></svg>ADD TO CART</a></div>
<div class="abs card" style="left:480px;top:849px"><div class="photo" role="img" aria-label="Blue and white mug with sun and clouds" style="background:linear-gradient(#7a7a7a,#a9bccc 50%,#9c8670)"><span class="price">$28</span></div><p class="title"><span>Cappuccino mug with daisies</span><br>(empty decor)</p><a class="buy" href="#"><svg viewBox="0 0 18 15"><path d="M1 1h3l2 8h9l2-6H5" fill="none" stroke="#fff" stroke-width="1.5"/><circle cx="7" cy="13" r="1.4" fill="#fff"/><circle cx="14" cy="13" r="1.4" fill="#fff"/></svg>ADD TO CART</a></div>

<div class="abs pager">Page 1 of 32 <span class="p on">1</span><span class="p">2</span><span class="p">3</span><span class="p">4</span><span class="p">5</span><span class="p">6</span><span class="p">7</span><span class="p">8</span><span class="p">»</span> … <span class="p">»»</span></div>

<section class="abs country">
  <h3>Select your Country</h3>
  <ul class="list">
    <li>Davidson, NC</li><li>Bratislava, SK</li>
    <li>Houston, TX</li><li>Edinburgh, UK</li>
    <li>La Crosse, WI</li><li>Tin Hau, Hong Kong</li>
    <li>Los Angeles, CA</li><li>Franfurkt am Main, DE</li>
  </ul>
  <div class="map" role="img" aria-label="World map marking store locations in North America, Europe and Asia"></div>
</section>

<section class="abs categories">
  <h3>Categories</h3>
  <ul class="list">
    <li>Animals</li><li>Meadow flowers</li>
    <li>Coffee beans</li><li>Stripes</li>
    <li>Daisies</li><li>Sun and clouds</li>
    <li>Hearts</li>
  </ul>
</section>

<nav class="abs footer-nav"><a href="#">Home</a>|<a href="#">Categories</a>|<a href="#">New Arrivals</a>|<a href="#">About our mugs</a>|<a href="#">My Account</a>|<a href="#">Contact Us</a></nav>
<p class="abs copyright">Copyright &nbsp;©&nbsp; 2013 &nbsp;&nbsp;www.tuliporchardwares.com &nbsp;&nbsp;&nbsp;All rights reserved.</p>
<a class="abs social" href="#" aria-label="Social page" style="left:857px"></a>
<a class="abs social" href="#" aria-label="Social feed" style="left:907px"></a>

</body>
</html>
```